Boom Way Hoist Service Business Cards

I need a business card for "Boom Way Hoist and Haulage"

Boomway2023@hoistmail.net

Hoist Works LLC, Boom Way Hoist and Haulage LLC

555.014.7260 | www.BOOMWAYHOISTS.example

Central Indiana & Northeast Ohio

(IN) 14820 Maple Lane Harlow Falls, IN 46000

(OH) 2450 Pell Street Cedar Bend, Ohio 44300

Colors
0094D4
00A9DD
6FCCEA
C7EBF8
E9F6FB
59FF00
82FF00
B8FF75
E3FFCB
F4FFEA
EE7325
F08F49
F5BC92
FAE3D3
FDF4ED
EB3D1F
EC4F4E
F09395
F8D3D4
FCEDEE
E54698
E96AAD
F1A4CE
F9D9EA
FCEFF6
A7469A
B969AE
D3A5CF
EDDBEB
F8F0F9

```html
<!DOCTYPE html>
<html lang="en">
<head>
<meta charset="utf-8">
<title>Boom Way Hoist Service Business Cards</title>
<link rel="stylesheet" href="https://fonts.googleapis.com/css2?family=Poppins:wght@400;600;700&display=swap">
<style>
  :root {
    --forest: #003009;
    --signal-red: #EB3D1F;
    --bright-green: #22C93A;
    --white: #FFFFFF;
    --ink: #1E1E1E;
    --page: #FFFFFF;
  }
  * { margin: 0; padding: 0; box-sizing: border-box; }
  html, body {
    width: 692px; height: 1200px; overflow: hidden;
    background: var(--page);
    font-family: "Poppins", sans-serif;
  }
  .sheet { position: relative; width: 692px; height: 1200px; }
  .card {
    position: absolute; left: 66px; width: 560px; height: 320px;
    overflow: hidden;
    box-shadow: 0 10px 24px rgba(0,0,0,.28);
  }
  .card--front { top: 250px; background: var(--forest); }
  .card--back { top: 630px; background: var(--forest); }

  /* front */
  .front-illustration {
    position: absolute; left: 200px; top: 58px; width: 160px; height: 100px;
    background: linear-gradient(160deg, #1f6b2a 0%, #22C93A 55%, #0d3f15 100%);
    opacity: .85;
  }
  .front-name {
    position: absolute; left: 0; right: 0; top: 166px;
    text-align: center; color: var(--white);
    font-weight: 700; font-size: 30px; letter-spacing: 2px;
  }
  .front-band {
    position: absolute; left: 0; right: 0; top: 224px; height: 37px;
    background: var(--signal-red);
    display: flex; align-items: center; justify-content: center;
  }
  .front-url {
    color: var(--white); font-weight: 600; font-size: 19px; letter-spacing: 3.6px;
  }

  /* back */
  .back-shapes { position: absolute; inset: 0; }
  .back-name {
    position: absolute; left: 28px; top: 108px; width: 170px;
    color: var(--white); font-weight: 700; font-size: 40px; line-height: 1.02;
    letter-spacing: 1px;
  }
  .back-title {
    position: absolute; left: 244px; top: 18px;
    color: var(--signal-red); font-weight: 700; font-size: 25px; line-height: 1.2;
  }
  .back-subtitle {
    position: absolute; left: 244px; top: 52px;
    color: var(--ink); font-weight: 400; font-size: 15.5px;
  }
  .contact-bar {
    position: absolute; right: 26px; height: 25px;
    background: var(--signal-red);
    display: flex; align-items: center;
    overflow: hidden;
  }
  .contact-bar__icon {
    flex: none;
    width: 36px; height: 25px; background: var(--forest);
    clip-path: polygon(0 0, 100% 0, 88% 100%, 8% 100%);
    display: flex; align-items: center; justify-content: center;
    margin-left: 4px;
  }
  .contact-bar__text {
    color: var(--white); font-size: 13px; margin-left: 8px; white-space: nowrap;
  }
  .contact-bar--phone { top: 86px; left: 256px; }
  .contact-bar--mail  { top: 121px; left: 266px; }
  .contact-bar--web   { top: 155px; left: 276px; }

  .office {
    position: absolute; left: 307px; display: flex; align-items: center;
  }
  .office--in { top: 200px; }
  .office--oh { top: 242px; }
  .office__region {
    width: 98px; font-weight: 700; font-size: 13.5px; line-height: 1.1; color: var(--ink);
  }
  .office__region span { display: block; color: var(--signal-red); }
  .office__divider { width: 1px; height: 28px; background: var(--ink); margin-right: 7px; }
  .office__address { font-size: 11.5px; line-height: 1.3; color: var(--ink); white-space: nowrap; }
</style>
</head>
<body>
<main class="sheet">

  <section class="card card--front" aria-label="Business card front">
    <div class="front-illustration" role="img" aria-label="Illustration of a mobile hoist with extended boom"></div>
    <div class="front-name">BOOM WAY</div>
    <div class="front-band"><span class="front-url">www.boomwayhoists.example</span></div>
  </section>

  <section class="card card--back" aria-label="Business card back">
    <svg class="back-shapes" width="560" height="320" viewBox="0 0 560 320" aria-hidden="true">
      <polygon points="207,0 560,0 560,320 305,320" fill="var(--white)"/>
      <polygon points="196,0 207,0 305,320 294,320" fill="var(--signal-red)"/>
      <polygon points="297,296 560,296 560,320 305,320" fill="var(--bright-green)"/>
    </svg>

    <div class="back-name">BOOM<br>WAY</div>

    <h1 class="back-title">HOIST WORKS LLC</h1>
    <p class="back-subtitle">Boom Way Hoist and Haulage LLC</p>

    <div class="contact-bar contact-bar--phone">
      <span class="contact-bar__icon">
        <svg width="13" height="13" viewBox="0 0 24 24"><path fill="#fff" d="M6.6 10.8a15 15 0 0 0 6.6 6.6l2.2-2.2c.3-.3.7-.4 1-.2 1.1.4 2.3.6 3.6.6.6 0 1 .4 1 1V20c0 .6-.4 1-1 1A17 17 0 0 1 3 4c0-.6.4-1 1-1h3.5c.6 0 1 .4 1 1 0 1.3.2 2.5.6 3.6.1.3 0 .7-.2 1z"/></svg>
      </span>
      <span class="contact-bar__text">555.014.7260</span>
    </div>
    <div class="contact-bar contact-bar--mail">
      <span class="contact-bar__icon">
        <svg width="13" height="10" viewBox="0 0 24 18"><rect width="24" height="18" rx="2" fill="#fff"/><path d="M1 2l11 8 11-8" stroke="var(--forest)" stroke-width="2" fill="none"/></svg>
      </span>
      <span class="contact-bar__text">Boomway2023@hoistmail.net</span>
    </div>
    <div class="contact-bar contact-bar--web">
      <span class="contact-bar__icon">
        <svg width="13" height="13" viewBox="0 0 24 24" fill="none" stroke="#fff" stroke-width="2"><circle cx="12" cy="12" r="10"/><ellipse cx="12" cy="12" rx="4" ry="10"/><path d="M2 12h20M4 7h16M4 17h16"/></svg>
      </span>
      <span class="contact-bar__text">www.BOOMWAYHOISTS.example</span>
    </div>

    <div class="office office--in">
      <div class="office__region">CENTRAL<span>INDIANA</span></div>
      <div class="office__divider"></div>
      <div class="office__address">14820 Maple Lane<br>Harlow Falls, IN 46000</div>
    </div>
    <div class="office office--oh">
      <div class="office__region">NORTHEAST<span>OHIO</span></div>
      <div class="office__divider"></div>
      <div class="office__address">2450 Pell Street<br>Cedar Bend, Ohio 44300</div>
    </div>
  </section>

</main>
</body>
</html>
```